依頼概要
「月見そら堂」は川越の蔵通りに佇み、熟練の和菓子職人がつくる豆菓子を専門に販売しています。創業から70年にわたり、手技による和菓子の技術と希少な地域食材を大切にしながら一粒一粒の豆の美味しさを守っています。
ブランドに関するその他情報やトンマナについては添付資料をご確認ください。

https://tsukimi-soradou.com/

<制作物>
A1ポスター
※採用者には追加で「横断幕」や「展示POP」等の制作を依頼させて頂きます。

<特徴>
①和菓子職人による手技で仕上げた希少な和菓子
②豆にこだわり、100種を超える豆菓子を製造し販売している
③和菓子の町でもある小江戸川越の歴史と文化を受け継いでいる
④「グルテンフリー」または「ローグルテン」の体に優しい菓子

<今施策のターゲット>
①日本文化に対して興味関心の高い「海外モダンラグジュアリー層」
②東南アジアに住む富裕層
③東南アジアで飲食店等を営み「上質で希少な甘味」を求める事業者

<主力商品>
①きなこまめ
月見そら堂の伝統和菓子。完熟空豆を一週間かけて蜜漬けを繰り返したお多福豆。豊潤で濃厚な和菓子の美味しさを味わえる。秩父産の幻の大豆「福寄せ大豆」を使用したきなこが、香ばしさを加える。

<依頼詳細>
海外展示会で使用する「ポスター」の制作をお願いします。
展示会への来場者が外国人となるため、使用する主言語は「英語」としてください。
採用者には

①ポスター
専門店感や多商品感(バラエティー感)の表現を1枚で行うのが難しい場合には、複数数のシリーズ化でのデザイン提案も可(最大5枚の展示が可能)
※基本的には1デザインの制作で問題ありません。

サイズ:A1(縦長)
訴求内容:豆菓子専門店、きなこまめ、伝統的な高級和菓子、グルテンフリー、健康食
シズル感:きなこまめからのシズル感
商品情報等:添付資料(Product)を参照

※その他注意点
ご納品方法:入稿データでの納品としてください。
入稿データのルールやテンプレートは下記URLよりご確認お願いします。

印刷会社 ポスター:ランプレス
https://www.lanpress.jp/lineup/poster

記載項目
ブランド名:Tsukimi Soradou
会社名: Hirata Co., Ltd.
ロゴ:添付ファイル
サイズ(ポスター):A1縦
サイズ(横断幕):幅2100mm 高900mm

添付資料
①Leaflet → ブランドに関する情報やトンマナを確認いただける資料
②Product → ロゴ・写真等の素材
③Others → その他素材
※納品データ制作時に高解像度のデータを提出いたします。

その他にも素材はありますので、必要素材がありましたらお知らせください。

-----追加で依頼をお願いする制作物例----
のぼり横断幕
採用となるデザインパターンは1種のみ。展示可能箇所が1か所のみとなるため、シリーズ化のデザインは不可。

サイズ:幅2100mm 高900mm
生地:テトロンポンジ
シズル感:きなこまめからのシズル感
その他:可能であれば店舗外観を挿入(国内店舗との関連想起を促すため)

海外展示会での使用に対してのバランス感の良さを評価させて頂きました。
また、参考資料とさせていただいたリーフレットとの融和性も高く、海外におけるブランディング構築効果が高いと判断させて頂きました。

ご提案して頂きました皆様、誠にありがとうございます。
選考上での修正につきましても迅速な対応をしていただけたこと、重ねて御礼申し上げます。
最後まで選出に苦慮するほどに素敵なご提案が多く、社員一同感激しております。
別の機会がございましたら、何卒、宜しくお願い致します。

```html
<!DOCTYPE html>
<html lang="en">
<head>
<meta charset="utf-8">
<title>Tsukimi Soradou — Premium Bean Sweets</title>
<link rel="stylesheet" href="https://fonts.googleapis.com/css2?family=Playfair+Display:wght@800&family=Shippori+Mincho:wght@500&family=Cormorant+Garamond:wght@500&display=swap">
<style>
  :root {
    --sky: #cddde7;
    --paper: #ffffff;
    --ink: #1b1b1d;
    --kinako: #d6bf98;
    --kinako-light: #e6d5b6;
    --bean: #2b1a1f;
    --bean-light: #4a3136;
  }
  * { margin: 0; padding: 0; box-sizing: border-box; }
  html, body { width: 846px; height: 1200px; overflow: hidden; background: var(--paper); }
  .poster {
    position: relative;
    width: 846px;
    height: 1200px;
    background: var(--paper);
    color: var(--ink);
    overflow: hidden;
  }
  .hero {
    position: absolute;
    left: 0; top: 0;
    width: 846px; height: 652px;
    background: var(--sky);
  }
  .kinako-photo {
    position: absolute;
    left: 110px; top: 115px;
    width: 290px; height: 200px;
    border-radius: 50%;
    background: radial-gradient(ellipse at 50% 45%, var(--kinako-light) 0%, var(--kinako) 55%, rgba(214,191,152,0) 72%);
  }
  .bean-photo {
    position: absolute;
    left: 445px; top: 90px;
    width: 300px; height: 275px;
    border-radius: 46% 54% 48% 52%;
    background: radial-gradient(ellipse at 40% 40%, var(--bean-light) 0%, var(--bean) 60%);
  }
  .brand-vertical {
    position: absolute;
    left: 585px; top: 420px;
    writing-mode: vertical-rl;
    font-family: "Shippori Mincho", serif;
    font-weight: 500;
    font-size: 50px;
    letter-spacing: 6px;
    color: var(--ink);
  }
  .headline {
    position: absolute;
    left: 0; top: 575px;
    width: 808px;
    text-align: center;
    font-family: "Playfair Display", serif;
    font-weight: 800;
    font-size: 80px;
    line-height: 71px;
    letter-spacing: 1px;
    color: var(--ink);
  }
  .gluten-note {
    position: absolute;
    left: 254px; top: 808px;
    width: 310px;
    padding: 7px 0 8px;
    border-top: 1px solid var(--ink);
    border-bottom: 1px solid var(--ink);
    text-align: center;
    font-family: "Cormorant Garamond", serif;
    font-weight: 500;
    font-size: 20px;
    color: var(--ink);
  }
  .signature {
    position: absolute;
    left: 0; top: 975px;
    width: 846px;
    display: flex;
    flex-direction: column;
    align-items: center;
    gap: 22px;
  }
  .signature-mark {
    width: 44px; height: 44px;
    border: 2px solid var(--ink);
    border-radius: 50%;
  }
  .signature-name {
    font-family: "Cormorant Garamond", serif;
    font-weight: 500;
    font-size: 22px;
    letter-spacing: 1px;
    color: var(--ink);
  }
</style>
</head>
<body>
  <main class="poster">
    <section class="hero">
      <div class="kinako-photo" role="img" aria-label="Photo of a small mound of golden kinako soybean flour"></div>
      <div class="bean-photo" role="img" aria-label="Photo of two glossy dark honey-soaked broad beans"></div>
      <p class="brand-vertical">月見そら堂</p>
    </section>
    <h1 class="headline">PREMIUM<br>BEAN<br>SWEETS</h1>
    <p class="gluten-note">All products are Gluten Free</p>
    <footer class="signature">
      <span class="signature-mark"></span>
      <span class="signature-name">tsukimi soradou</span>
    </footer>
  </main>
</body>
</html>
```